My Book needs a front and back cover design

I need you to design my front and back cover of my book. The title of my book is : Lanterns Past Harbour
Tide Notes
7 paths to gardening calmly always

The picture that I uploaded needs to be on the front cover. On the back cover it should be excerpt from Chapter One like this :

As years have gone by I have become much more conscious about my problem with stuttering, more able to relax my muscles to alleviate it. At the age of 20, I realized that stuttering is like a demon in my head that needs to be killed and that nothing is wrong with me. Furthermore, no one can help me but myself. I'm holding the key of my future. Everything is just in my head.

With this book, I want to help you realize that nobody can help you fix your stuttering better than yourself. There's no quick-get-rid-of-stuttering cure. The cure lies inside of you.

- Lorcan Vittel, excerpt from Chapter One
----------------------------------------------------------------------------------

My name also needs to be located on the front cover.

Target Market(s)

80 million people who stutter each day

Industry/Entity Type

Psychology

Font styles to use
Serif
Sans Serif

Colors
1b1b1b
000000
333333

Requirements
Must have
• Front Cover : Full Title and subtitle and my name and my picture
• Back Cover : Excerpt from my Chapter One with my name below just as I have described in my project description
Nice to have
• Maybe black background would be the best for the front cover.

```html
<!DOCTYPE html>
<html lang="en">
<head>
<meta charset="utf-8">
<title>Lanterns Past Harbour — Tide Notes, cover spread</title>
<link rel="stylesheet" href="https://fonts.googleapis.com/css2?family=Oswald:wght@400;500;600&family=Libre+Baskerville:ital,wght@0,400;0,700;1,400&display=swap">
<style>
  :root {
    --stage: #e9e9e9;
    --ink: #1b1b1b;
    --black: #000000;
    --charcoal: #333333;
    --paper: #ffffff;
    --accent-red: #e0262b;
    --soft-grey: #9a9a9a;
    --spine-light: #bdbdbd;
    --spine-dark: #8e8e8e;
    --title-sans: "Oswald", "Arial Narrow", sans-serif;
    --body-serif: "Libre Baskerville", Georgia, serif;
  }
  * { box-sizing: border-box; margin: 0; padding: 0; }
  html, body {
    width: 1130px; height: 1200px; overflow: hidden;
    background: var(--stage);
  }
  .spread {
    position: absolute; left: 40px; top: 200px;
    width: 1050px; height: 800px;
    display: flex;
    box-shadow: 0 20px 40px rgba(0,0,0,.18);
  }

  /* Back cover */
  .back-cover {
    width: 500px; height: 100%;
    background: var(--paper);
    color: var(--ink);
    padding: 150px 54px 0;
    font-family: var(--body-serif);
    text-align: center;
  }
  .excerpt-lead {
    font-weight: 700; font-size: 17px; line-height: 1.45;
    margin-bottom: 30px;
  }
  .excerpt-body {
    font-style: italic; font-size: 14px; line-height: 1.55;
    margin-bottom: 30px; color: var(--charcoal);
  }
  .excerpt-body.plain { font-style: normal; font-size: 14.5px; margin-bottom: 6px; }
  .excerpt-close {
    font-weight: 700; font-size: 21px; margin: 4px 0 22px;
  }
  .excerpt-credit {
    text-align: right; font-size: 13px; line-height: 1.4; color: var(--charcoal);
    padding-right: 10px;
  }

  /* Spine */
  .spine {
    width: 50px; height: 100%;
    background: linear-gradient(90deg, var(--spine-dark), var(--spine-light) 45%, var(--spine-dark));
    display: flex; align-items: center; justify-content: center;
  }
  .spine-text {
    writing-mode: vertical-rl;
    font-family: var(--title-sans); font-weight: 500;
    font-size: 19px; letter-spacing: .5px; text-transform: uppercase;
    white-space: nowrap; color: var(--black);
  }
  .spine-text .light { color: var(--paper); }
  .spine-text .red { color: var(--accent-red); }

  /* Front cover */
  .front-cover {
    position: relative;
    width: 500px; height: 100%;
    background: var(--black);
    overflow: hidden;
    text-align: center;
  }
  .series-title {
    position: relative; z-index: 2;
    margin-top: 40px;
    font-family: var(--title-sans); font-weight: 600;
    font-size: 42px; line-height: 1; letter-spacing: .5px;
    text-transform: uppercase; color: var(--paper);
  }
  .series-title .mid { color: var(--soft-grey); }
  .series-title .red { color: var(--accent-red); }
  .author-portrait {
    position: absolute; left: 40px; top: 95px;
    width: 420px; height: 500px;
    background: radial-gradient(ellipse 55% 60% at 50% 40%, #3a3a3a 0%, #1b1b1b 55%, #000 100%);
  }
  .book-title {
    position: absolute; left: 0; right: 0; top: 575px;
    font-family: var(--body-serif); font-weight: 700;
    font-size: 66px; line-height: 1; color: var(--paper);
    text-transform: uppercase; letter-spacing: 1px;
  }
  .book-subtitle {
    position: absolute; left: 0; right: 0; top: 650px;
    font-family: var(--title-sans); font-weight: 500;
    font-size: 24px; text-transform: uppercase; color: var(--paper);
    letter-spacing: .5px;
  }
  .book-subtitle .red { color: var(--accent-red); }
  .author-name {
    position: absolute; left: 0; right: 0; bottom: 38px;
    font-family: var(--body-serif); font-size: 25px;
    letter-spacing: 2px; text-transform: uppercase; color: #b5b5b5;
  }
</style>
</head>
<body>
  <main class="spread">
    <section class="back-cover">
      <p class="excerpt-lead">As years have gone by I have become much more conscious about my problem with stuttering, more able to relax my muscles to alleviate it.</p>
      <p class="excerpt-body">At the age of 20, I realized that stuttering is like a demon in my head that needs to be killed and that nothing is wrong with me. Furthermore, no one can help me but myself. I'm holding the key of my future. Everything is just in my head.</p>
      <p class="excerpt-body plain">With this book, I want to help you realize that nobody can help you fix your stuttering better than yourself. There's no quick-get-rid-of-stuttering cure.</p>
      <p class="excerpt-close">The cure lies inside of you.</p>
      <p class="excerpt-credit">Lorcan Vittel<br><em>excerpt from Chapter One</em></p>
    </section>

    <section class="spine">
      <p class="spine-text">Lorcan Vittel <span class="light">Lanterns Past Harbour</span> Tide Notes: <span class="red">7 Paths</span> to gardening calmly <span class="red">always</span></p>
    </section>

    <section class="front-cover">
      <h2 class="series-title">Lanterns <span class="mid">Past</span> <span class="red">Harbour</span></h2>
      <div class="author-portrait" role="img" aria-label="Portrait photograph of the author in a black polo shirt against a dark background"></div>
      <h1 class="book-title">Tide Notes</h1>
      <p class="book-subtitle"><span class="red">7 Paths</span> to gardening calmly <span class="red">always</span></p>
      <p class="author-name">Lorcan Vittel</p>
    </section>
  </main>
</body>
</html>
```